Postcard Design Project

Education- charter school- elementary k-6th grades- performing arts integrated in to the core curriculum

Industry/Entity Type

School

```html
<!DOCTYPE html>
<html lang="en">
<head>
<meta charset="utf-8">
<title>Bright Stage Arts Academy – Enrollment Postcard</title>
<link rel="stylesheet" href="https://fonts.googleapis.com/css2?family=Source+Sans+3:wght@400;700&family=Questrial&display=swap">
<style>
  :root {
    --backdrop: #ececec;
    --paper: #ffffff;
    --violet: #5e4fa2;
    --magenta: #b24f9f;
    --lemon: #efe817;
    --ink: #2b2a5c;
    --lavender-text: #5646a8;
    --band: rgba(200, 190, 235, 0.28);
    --star: #e9e21a;
  }
  * { margin: 0; padding: 0; box-sizing: border-box; }
  html, body { width: 1200px; height: 783px; overflow: hidden; background: var(--backdrop); }
  .canvas { position: relative; width: 1200px; height: 783px; }

  .page {
    position: absolute; top: 34px; width: 488px; height: 709px;
    background: var(--paper); overflow: hidden;
  }
  .page--front { left: 56px; }
  .page--back { left: 657px; }
  .page svg.art { position: absolute; inset: 0; }

  .brand {
    position: absolute; left: 0; right: 0; top: 92px;
    display: flex; align-items: center; justify-content: center; gap: 8px;
    font-family: "Source Sans 3", sans-serif; font-weight: 400;
    font-size: 15px; color: var(--ink);
  }
  .brand__dot { width: 12px; height: 12px; border-radius: 50%; background: var(--violet); }

  .headline {
    position: absolute; left: 28px; top: 326px;
    font-family: "Source Sans 3", sans-serif; font-weight: 700;
    font-size: 35px; line-height: 48px; color: #fff;
  }
  .front-contact {
    position: absolute; left: 89px; top: 577px;
    font-family: "Source Sans 3", sans-serif; color: #fff;
  }
  .front-contact__name { font-size: 22px; line-height: 25px; margin-bottom: 8px; }
  .front-contact__line { font-size: 13px; line-height: 16px; }

  .back-body {
    position: absolute; left: 32px; top: 184px; width: 418px;
    display: flex; flex-direction: column; align-items: center;
    font-family: "Questrial", sans-serif; color: var(--lavender-text);
    font-size: 12px; line-height: 19.5px; text-align: center;
  }
  .back-body__star { width: 20px; height: 19px; margin: 2px 0 1px; }
  .back-body__point { width: 100%; background: var(--band); padding: 1px 6px; }

  .back-contact {
    position: absolute; left: 0; right: 0; top: 587px;
    font-family: "Questrial", sans-serif; color: var(--lavender-text);
    font-size: 18px; line-height: 20px; text-align: center;
  }
</style>
</head>
<body>
<main class="canvas">

  <section class="page page--front">
    <svg class="art" width="488" height="709" viewBox="0 0 488 709">
      <defs>
        <linearGradient id="front-wash" x1="0" y1="0" x2="1" y2="1">
          <stop offset="0" stop-color="#e6f4fb"/>
          <stop offset="0.6" stop-color="#ffffff"/>
          <stop offset="1" stop-color="#f3f7da"/>
        </linearGradient>
        <linearGradient id="kids-photo" x1="0" y1="0" x2="1" y2="0">
          <stop offset="0" stop-color="#f2b25a"/>
          <stop offset="0.5" stop-color="#e7785d"/>
          <stop offset="1" stop-color="#d9475b"/>
        </linearGradient>
        <linearGradient id="silhouette-photo" x1="0" y1="0" x2="0" y2="1">
          <stop offset="0" stop-color="#e9f3c8"/>
          <stop offset="0.45" stop-color="#6b3a2e"/>
          <stop offset="1" stop-color="#c7381f"/>
        </linearGradient>
      </defs>
      <rect width="488" height="709" fill="url(#front-wash)"/>
      <rect x="40" y="130" width="446" height="200" rx="60" fill="url(#kids-photo)" opacity="0.55"
            role="img" aria-label="Photo of children jumping joyfully in colourful clothes"/>
      <polygon points="266,272 486,103 486,466 334,514" fill="url(#silhouette-photo)"
               role="img" aria-label="Photo of dancing children in silhouette against a warm sunset glow"/>
      <polygon points="0,276 238,206 316,478 31,564 0,564" fill="var(--violet)"/>
      <polygon points="36,577 318,494 387,709 77,709" fill="var(--magenta)"/>
      <polygon points="344,522 486,474 486,709 399,709" fill="var(--lemon)"/>
    </svg>
    <div class="brand"><span class="brand__dot"></span>Bright Stage Arts Academy</div>
    <h1 class="headline">Now Enrolling<br>2016-17 for<br>Grades k-6th</h1>
    <div class="front-contact">
      <p class="front-contact__name">Bright Stage Arts<br>Academy</p>
      <p class="front-contact__line">270 Maple Hollow Road</p>
      <p class="front-contact__line">Riverton, Ohio 43100</p>
      <p class="front-contact__line">Phone: (555) 014-2290</p>
    </div>
  </section>

  <section class="page page--back">
    <svg class="art" width="488" height="709" viewBox="0 0 488 709">
      <defs>
        <linearGradient id="back-wash" x1="0" y1="0" x2="1" y2="1">
          <stop offset="0" stop-color="#e8f4fb"/>
          <stop offset="0.55" stop-color="#f7f4fb"/>
          <stop offset="1" stop-color="#f7f8e4"/>
        </linearGradient>
      </defs>
      <rect width="488" height="709" fill="#fff"/>
      <rect y="155" width="488" height="554" fill="url(#back-wash)"/>
      <polygon points="0,300 250,230 330,500 30,590" fill="#ece8f6" opacity="0.7"/>
      <polygon points="44,580 330,500 400,709 84,709" fill="#f1e3ef" opacity="0.7"/>
      <polygon points="350,520 488,470 488,709 400,709" fill="#f6f5d4" opacity="0.7"/>
    </svg>
    <div class="brand"><span class="brand__dot"></span>Bright Stage Arts Academy</div>
    <div class="back-body">
      <svg class="back-body__star" viewBox="0 0 20 19"><polygon points="10,0 12.4,7 20,7 13.8,11.4 16.2,19 10,14.4 3.8,19 6.2,11.4 0,7 7.6,7" fill="var(--star)"/></svg>
      <p class="back-body__point">Bright Stage Arts Academy is the most innovative public elementary school program in Central Ohio through integration of the fine arts in all subjects.</p>
      <svg class="back-body__star" viewBox="0 0 20 19"><polygon points="10,0 12.4,7 20,7 13.8,11.4 16.2,19 10,14.4 3.8,19 6.2,11.4 0,7 7.6,7" fill="var(--star)"/></svg>
      <p class="back-body__point">All grade levels take visual arts, music, drama, and dance.</p>
      <svg class="back-body__star" viewBox="0 0 20 19"><polygon points="10,0 12.4,7 20,7 13.8,11.4 16.2,19 10,14.4 3.8,19 6.2,11.4 0,7 7.6,7" fill="var(--star)"/></svg>
      <p class="back-body__point">Small class sizes with Highly Qualified teachers in the core subjects, beautiful facilities with a five acre campus provide for an outdoor learning experience, and a dedicated staff committed to a positive learning environment are just a few reasons that you will be amazed by this performing arts community school.</p>
      <svg class="back-body__star" viewBox="0 0 20 19"><polygon points="10,0 12.4,7 20,7 13.8,11.4 16.2,19 10,14.4 3.8,19 6.2,11.4 0,7 7.6,7" fill="var(--star)"/></svg>
      <p class="back-body__point">Breakfast and lunch are provided at no cost to you! All of this tuition free! Please contact us for a tour of our school.</p>
      <svg class="back-body__star" viewBox="0 0 20 19"><polygon points="10,0 12.4,7 20,7 13.8,11.4 16.2,19 10,14.4 3.8,19 6.2,11.4 0,7 7.6,7" fill="var(--star)"/></svg>
      <p class="back-body__point">Classes fill up quickly so call today to ensure your child's enrollment for the 2016-17 school year.</p>
    </div>
    <div class="back-contact">
      <p>270 Maple Hollow Road</p>
      <p>Riverton, Ohio 43100</p>
      <p>Phone: (555) 014-2290</p>
    </div>
  </section>

</main>
</body>
</html>
```